Career development coaching - school lever to adults, needs a business card

Tandel Grove - An independent Career Advice business that provides 1-2-1 advice,for career development, entrepreneurial support and workshops needs a business card. Our clients of all ages (school leaver to adults looking for a career move) and universities and colleges. We would like the card to be double-sided with a modern, professional look. Looking for something professional yet very creative and original. Want a standard size business card that inspires a second look because it stands out from the rest.

One side of the card to have a design incorporating the logo with Tandel Grove name with the strap line “Helping you find your future” and space for the company website

Other side of the card to the logo/Tandel Grove name and the usual contact information:
Individual Name
Job Title (for example, Director)
Phone number
Email address
Company website address

Facebook, LinkedIn and Twitter links will need to go somewhere (back or front!)

The design will be used for 3 individuals so should be editable so that we can update as needed/as we grow.

Attached is the company logo/colours to be incorporated.

Target Market(s)

1-2-1 advice,for career development, entrepreneurial support and workshops needs a business card. Our clients of all ages (school leaver to adults looking for a career move) and universities and colleges.

Industry/Entity Type

Consulting

Contact Information for Business Card

Individual Name
Phone number
Email address
Company website address

Font styles to use
Sans Serif

Colors
0255a3
3176b5
faa54b
f78f20
85acd3
cfdeed

Requirements
Must have
• use the Tandel Grove Logo in some way - using the colours and the blue/orange palette
• For the logo - hope this makes sense to someone or if they direclty relate to the logo image attached!
• For the Orange:- Pantone 1585 C
• In CMYK : C3 M71 Y100 K0
• For the Blue:- 100% Pantone 7469 C
• In CMYK : C100 M62 Y27 K7
• Please feel free to contact me with any questions for more info
Nice to have
• happy to see any creative designs
Should not have
• Nothing too traditional,

```html
<!DOCTYPE html>
<html lang="en">
<head>
<meta charset="utf-8">
<title>Tandel Grove – Business Card</title>
<link href="https://fonts.googleapis.com/css2?family=Source+Sans+3:wght@400;600&display=swap" rel="stylesheet">
<style>
  :root {
    --blue: #0f6590;
    --orange: #ec7035;
    --white: #ffffff;
    --ink: #3a3a3a;
    --backdrop: #5e4a3d;
    --font: "Source Sans 3", sans-serif;
  }
  * { box-sizing: border-box; margin: 0; padding: 0; }
  html, body {
    width: 1200px; height: 987px; overflow: hidden;
    background: var(--backdrop);
    font-family: var(--font);
  }
  .canvas { position: relative; width: 1200px; height: 987px; }

  .card {
    position: absolute; left: 293px; width: 615px; height: 352px;
    box-shadow: 0 3px 10px rgba(0,0,0,.35);
    overflow: hidden;
  }
  .card--front { top: 130px; background: var(--white); }
  .card--back { top: 505px; background: var(--blue); }

  /* front */
  .brand-dot {
    position: absolute; left: 50%; top: 28px; width: 96px; height: 96px;
    margin-left: -48px; border-radius: 50%; background: var(--blue);
  }
  .brand-name {
    position: absolute; left: 0; right: 0; top: 140px;
    text-align: center; font-size: 29px; font-weight: 400;
    font-variant: small-caps; letter-spacing: 1.5px; color: var(--blue);
  }
  .name-band {
    position: absolute; top: 201px; height: 47px; left: 0; right: 0;
  }
  .name-band__person {
    position: absolute; left: 0; width: 305px; height: 100%;
    background: var(--blue); color: var(--white);
    font-size: 22px; font-weight: 600; text-transform: uppercase;
    text-align: right; padding-right: 14px; line-height: 47px;
  }
  .name-band__role {
    position: absolute; left: 310px; right: 0; height: 100%;
    background: var(--orange); color: var(--white);
    font-size: 16px; text-transform: uppercase;
    padding-left: 14px; line-height: 47px;
  }
  .contacts, .socials {
    position: absolute; top: 266px; list-style: none;
    font-size: 16.5px; color: var(--ink);
  }
  .contacts { left: 34px; }
  .socials { right: 30px; text-align: right; }
  .contacts li, .socials li {
    height: 23.5px; display: flex; align-items: center; gap: 7px;
  }
  .socials li { justify-content: flex-end; }
  .icon { width: 15px; height: 15px; flex: none; }
  .social-dot {
    width: 20px; height: 20px; border-radius: 50%;
    background: var(--blue); flex: none;
  }

  /* back */
  .back-half {
    position: absolute; left: 0; top: 0; bottom: 0; width: 307px;
    background: var(--orange);
  }
  .back-dot {
    position: absolute; left: 50%; top: 100px; width: 104px; height: 104px;
    margin-left: -52px; border-radius: 50%; background: var(--white);
  }
  .back-name {
    position: absolute; left: 0; right: 0; top: 224px; text-align: center;
    font-size: 33px; font-variant: small-caps; letter-spacing: 1.5px;
    color: var(--white);
  }
  .tagline {
    position: absolute; left: 0; right: 0; top: 270px; text-align: center;
    font-size: 18px; color: var(--white);
  }
</style>
</head>
<body>
<main class="canvas">

  <section class="card card--front" aria-label="Card front">
    <div class="brand-dot"></div>
    <div class="brand-name">Tandel Grove</div>

    <div class="name-band">
      <div class="name-band__person">Maren Holt</div>
      <div class="name-band__role">CEO/Founder</div>
    </div>

    <ul class="contacts">
      <li>
        <svg class="icon" viewBox="0 0 16 16" aria-hidden="true"><path fill="#0f6590" d="M3.6 1.2 6 3.6c.4.4.4 1 0 1.4L4.9 6.1c.8 1.9 3 4.1 5 5L11 10c.4-.4 1-.4 1.4 0l2.4 2.4c.4.4.4 1 0 1.4l-1.3 1.3c-.9.9-3 .6-5.8-1.6C5 11.2 2.6 8.3 1.6 5.9.9 4.2.9 3 1.6 2.3l.6-.6 1.4-.5z"/></svg>
        555 014 2290
      </li>
      <li>
        <svg class="icon" viewBox="0 0 16 16" aria-hidden="true"><rect x="1" y="3" width="14" height="10" fill="#0f6590"/><path d="M1.5 3.6 8 8.6l6.5-5" fill="none" stroke="#fff" stroke-width="1.3"/></svg>
        mholt@tandelgrove.com
      </li>
      <li>
        <svg class="icon" viewBox="0 0 16 16" aria-hidden="true"><circle cx="8" cy="8" r="7" fill="#0f6590"/><path d="M1 8h14M8 1c-2.6 3-2.6 11 0 14M8 1c2.6 3 2.6 11 0 14" fill="none" stroke="#fff" stroke-width="1"/></svg>
        www.tandelgrove.com
      </li>
    </ul>

    <ul class="socials">
      <li>pageloop.com/tandelgrove <span class="social-dot"></span></li>
      <li>worknest.com/tandelgrove <span class="social-dot"></span></li>
      <li>chirpline.com/tandelgroveuk <span class="social-dot"></span></li>
    </ul>
  </section>

  <section class="card card--back" aria-label="Card back">
    <div class="back-half"></div>
    <div class="back-dot"></div>
    <div class="back-name">Tandel Grove</div>
    <div class="tagline">Professional Career Consultancy</div>
  </section>

</main>
</body>
</html>
```